Graphic Design Banners for my newsletters: Thermomugs

We sell merchandise to business costumers. We will send newsletters every week, and I need to find someone who can make me nice banners to my newsletters.The goal with my newsletters is to SELL the products and introduce costumers to my website: www.fernvalegoods.dk. I need 3 banners to my newsletters about thermomugs:* Banner 1 - Model 37250. I think an orange round price splash (69,- v/100 stk) with this text: "Drypfri og dobbeltvægget Termokrus i rustfri stål ude og PP inde med push funktion i lækkert design."* Banner 2 - Model 82713. I think an orange round price splash (49,- v/100 stk) with this text: "Dobbeltvægget Termokrus i PP plastik i 4 forskellige farver."* Banner 3 - KT3176. Bubble price splash (45,- v/100 stk) and this text: "Dobbeltvægget termokrus med hank. Rustfri stål ude og PP inde."Maybe it will be nice if it has a "call to action" BESTIL HER (in English, it means ORDER HERE) on each banner. Here, I've attached pictures for all 3 thermomugs. The filename is the modelnumber and I sent you pictures of how it appears right now in our newsletters, and I need you to make them nicer. Personally, I like the "R&J better than the other we made." but I need help, since it looks bad and unprofessional.Thank you.

Target Market(s)

Big and middle Big companies.

Industry/Entity Type

Promotional Merchandise

Colors
faa54b

Requirements
Must have
• I sent the newletters to marketing bosses so they like Nice style and proffesionalisme. They buy my products with there logo printed on. So the product details (Nice pictures) is importent to be in focus.
Nice to have
• I have sent some banners i use on my website. I like that style. But This to newletters Could be more kvadrat.

```html
<!DOCTYPE html>
<html lang="da">
<head>
<meta charset="utf-8">
<title>Termokrus – Drypfri og dobbeltvægget</title>
<link rel="stylesheet" href="https://fonts.googleapis.com/css2?family=Antonio:wght@100;200&family=Bebas+Neue&display=swap">
<style>
  :root {
    --orange: #f7861c;
    --orange-light: #faa54b;
    --cream: #f6f1ea;
    --black: #111111;
    --ribbon: #1a1a1a;
    --white: #ffffff;
    --grey-text: #bdbdbd;
  }
  html, body {
    margin: 0;
    padding: 0;
    overflow: hidden;
  }
  .banner {
    position: relative;
    width: 1200px;
    height: 955px;
    overflow: hidden;
    background: radial-gradient(ellipse at 45% 20%, var(--orange-light) 0%, var(--orange) 70%);
  }
  .banner > svg {
    position: absolute;
    left: 0;
    top: 0;
  }
  .headline-main {
    font-family: "Bebas Neue", sans-serif;
    font-size: 98px;
    fill: var(--white);
  }
  .headline-sub {
    font-family: "Bebas Neue", sans-serif;
    font-size: 40px;
    fill: var(--white);
  }
  .feature {
    font-family: "Antonio", sans-serif;
    font-weight: 100;
    fill: var(--grey-text);
  }
  .feature-material { font-size: 52px; }
  .feature-push { font-size: 76px; }
  .cta-label {
    font-family: "Bebas Neue", sans-serif;
    font-size: 66px;
    fill: var(--white);
  }
  .price-amount {
    font-family: "Bebas Neue", sans-serif;
    font-size: 78px;
    fill: var(--white);
  }
  .price-unit {
    font-family: "Bebas Neue", sans-serif;
    font-size: 28px;
    fill: var(--white);
  }
</style>
</head>
<body>
<main class="banner">
  <svg width="1200" height="955" viewBox="0 0 1200 955">
    <defs>
      <radialGradient id="splashFill" cx="0.45" cy="0.55" r="0.6">
        <stop offset="0" stop-color="#ffffff"/>
        <stop offset="1" stop-color="#f6f1ea"/>
      </radialGradient>
    </defs>

    <g class="corner-stripes">
      <polygon points="0,60 130,0 175,0 0,82" fill="var(--black)"/>
      <polygon points="0,112 240,0 268,0 0,138" fill="var(--black)"/>
    </g>

    <g class="product-photo" role="img" aria-label="Produktfoto: hvidt og sort termokrus med låg, samt adskilte dele (låg, indersæt og stålkop) på hvid malingsplet">
      <path d="M70,110 L230,95 L420,135 L560,125 L640,170 L700,240 L760,330 L820,420 L880,500 L930,610 L960,700 L900,760 L820,830 L700,870 L560,880 L420,860 L300,880 L160,850 L60,800 L10,700 L0,560 L20,400 L0,300 L30,200 Z" fill="url(#splashFill)"/>
      <rect x="108" y="186" width="220" height="600" rx="40" fill="#eeeeee"/>
      <rect x="255" y="246" width="240" height="602" rx="40" fill="#2a2626"/>
      <rect x="515" y="570" width="160" height="90" rx="30" fill="#d8d8d8"/>
      <rect x="560" y="680" width="80" height="75" rx="18" fill="#3a3a3a"/>
      <rect x="688" y="640" width="140" height="105" rx="30" fill="#8a8a8a"/>
    </g>

    <g class="price-splash">
      <circle cx="628" cy="440" r="100" fill="var(--orange)"/>
      <circle cx="628" cy="440" r="90" fill="none" stroke="var(--white)" stroke-width="2"/>
      <text class="price-amount" x="628" y="458" text-anchor="middle">69,-</text>
      <text class="price-unit" x="628" y="492" text-anchor="middle">v/100 stk</text>
    </g>

    <polygon class="ribbon" points="764,0 1164,0 1164,568 964,480 764,568" fill="var(--ribbon)"/>

    <g class="ribbon-text">
      <text class="headline-main" x="792" y="104" textLength="340" lengthAdjust="spacingAndGlyphs">DRYPFRI OG</text>
      <text class="headline-sub" x="802" y="152" textLength="326" lengthAdjust="spacing">DOBBELTVÆGGET</text>
      <text class="feature feature-material" x="798" y="236" textLength="328" lengthAdjust="spacingAndGlyphs">TERMOKRUS I RUSTFRI</text>
      <text class="feature feature-material" x="798" y="284" textLength="332" lengthAdjust="spacingAndGlyphs">STÅL UDE OG PP INDE MED</text>
      <text class="feature feature-push" x="804" y="392" textLength="322" lengthAdjust="spacingAndGlyphs">PUSH FUNKTION</text>
      <text class="feature feature-push" x="804" y="452" textLength="324" lengthAdjust="spacingAndGlyphs">I LÆKKERT DESIGN</text>
    </g>

    <g class="cta-tag">
      <polygon points="1110,955 1200,890 1200,920 1150,955" fill="var(--black)"/>
      <polygon points="1050,955 1200,850 1200,868 1075,955" fill="var(--black)"/>
      <polygon points="856,808 1200,808 1200,896 856,896 904,852" fill="var(--black)"/>
      <a href="#">
        <text class="cta-label" x="926" y="876" textLength="236" lengthAdjust="spacingAndGlyphs">BESTIL HER</text>
      </a>
    </g>
  </svg>
</main>
</body>
</html>
```